Business card and stationary for tattoo photography company
Velvet Harbor Photography
Modern
Marco Delvane
Photographer / Owner
4783 Willowmere Ln Larkmoor, GA 30599
marco@velvetharborphotography.com
www.velvetharborphotography.com
Grace, Grit, and Artistry

```html
<!DOCTYPE html>
<html lang="en">
<head>
<meta charset="utf-8">
<title>Velvet Harbor Photography – Business Card</title>
<link href="https://fonts.googleapis.com/css2?family=Open+Sans:wght@400;600;700&display=swap" rel="stylesheet">
<style>
  :root {
    --backdrop: #3a3a3c;
    --card-black: #151314;
    --band-dark: #2b2b2c;
    --accent-red: #c4161c;
    --paper: #f1eff1;
    --tagline-tan: #d9b48a;
    --muted-grey: #a9a6a8;
    --ink: #1c1c1c;
    --photo-warm: #6e4a48;
    --photo-violet: #7b5f96;
    --photo-faded: #d9d3da;
  }
  * { box-sizing: border-box; margin: 0; padding: 0; }
  html, body {
    width: 1200px; height: 795px; overflow: hidden;
    background: var(--backdrop);
    font-family: "Open Sans", Arial, sans-serif;
  }
  .canvas {
    width: 1200px; height: 795px;
    display: flex; align-items: center; justify-content: center; gap: 60px;
  }
  .card {
    position: relative; width: 520px; height: 297px;
    border-radius: 18px; overflow: hidden;
    box-shadow: 0 10px 24px rgba(0,0,0,.45);
  }

  /* Front */
  .card-front { background: var(--card-black); }
  .front-photo {
    position: absolute; left: 0; bottom: 0; width: 320px; height: 210px;
    background:
      radial-gradient(ellipse at 30% 40%, var(--photo-violet) 0%, transparent 45%),
      radial-gradient(ellipse at 55% 65%, var(--photo-warm) 0%, transparent 70%),
      linear-gradient(135deg, #3b2b2d, #1a1517 80%);
    -webkit-mask-image: linear-gradient(to right, #000 60%, transparent);
            mask-image: linear-gradient(to right, #000 60%, transparent);
  }
  .front-brand {
    position: absolute; right: 30px; top: 56px; width: 300px; text-align: center;
  }
  .brand-name {
    color: #ffffff; font-weight: 600; font-size: 30px; line-height: 1.1;
    letter-spacing: .5px;
  }
  .brand-rule {
    display: flex; align-items: center; gap: 8px; margin-top: 6px;
    color: #ffffff; font-size: 10px; letter-spacing: 4px;
  }
  .brand-rule::before, .brand-rule::after {
    content: ""; flex: 1; height: 1px; background: #ffffff;
  }
  .tagline {
    margin-top: 22px; color: var(--tagline-tan); font-weight: 600; font-size: 15px;
  }
  .front-web {
    margin-top: 10px; color: var(--muted-grey); font-size: 12px;
  }

  /* Back */
  .card-back { background: var(--paper); }
  .back-photo {
    position: absolute; inset: 0;
    background:
      radial-gradient(ellipse at 80% 75%, #c9bfd0 0%, transparent 55%),
      radial-gradient(ellipse at 15% 85%, #e2c7c2 0%, transparent 45%),
      var(--photo-faded);
    opacity: .75;
  }
  .back-band {
    position: absolute; left: 0; right: 0; top: 34px; height: 112px;
    background: var(--band-dark);
    border-top: 3px solid var(--accent-red);
    border-bottom: 3px solid var(--accent-red);
    display: flex; flex-direction: column; align-items: center; justify-content: center;
  }
  .back-band::before, .back-band::after {
    content: ""; position: absolute; left: 0; right: 0; height: 1px;
  }
  .back-band::before { top: -8px; background: var(--accent-red); }
  .back-band::after { bottom: -8px; background: #555; }
  .back-band .brand-name { font-size: 28px; }
  .back-band .brand-rule { width: 300px; }
  .back-details {
    position: absolute; left: 150px; top: 162px; color: var(--ink);
  }
  .person-name { color: var(--accent-red); font-weight: 700; font-size: 18px; line-height: 1.3; }
  .person-title { font-size: 12.5px; margin-bottom: 12px; }
  .contact-line {
    display: flex; align-items: center; gap: 6px; font-size: 11.5px; line-height: 1.7;
  }
  .contact-item { display: inline-flex; align-items: center; gap: 5px; }
  .contact-item + .contact-item { margin-left: 6px; }
  .contact-line svg { width: 11px; height: 11px; flex: none; }
</style>
</head>
<body>
<main class="canvas">

  <section class="card card-front">
    <div class="front-photo" role="img" aria-label="Portrait photograph of a tattooed model seen from behind"></div>
    <div class="front-brand">
      <div class="brand-name">Velvet Harbor</div>
      <div class="brand-rule">PHOTOGRAPHY</div>
      <p class="tagline">Grace, Grit, and Artistry</p>
      <p class="front-web">www.velvetharborphotography.com</p>
    </div>
  </section>

  <section class="card card-back">
    <div class="back-photo" role="img" aria-label="Faded photograph of a tattooed arm and shoulder"></div>
    <div class="back-band">
      <div class="brand-name">Velvet Harbor</div>
      <div class="brand-rule">PHOTOGRAPHY</div>
    </div>
    <div class="back-details">
      <p class="person-name">Marco Delvane</p>
      <p class="person-title">Photographer / Owner</p>
      <p class="contact-line">4783 Willowmere Ln Larkmoor, GA 30599</p>
      <p class="contact-line">
        <span class="contact-item">
          <svg viewBox="0 0 12 12" aria-hidden="true"><circle cx="6" cy="6" r="6" fill="#1c1c1c"/><path d="M4 3.2c.4 1.9 1.6 3.5 3.6 4.6l.9-.9 1 .7-.6 1.1C6.3 8.6 3.9 6.1 3.3 3.6l1-.7z" fill="#fff"/></svg>
          (555) 019-4821
        </span>
        <span class="contact-item">
          <svg viewBox="0 0 12 12" aria-hidden="true"><circle cx="6" cy="6" r="6" fill="#1c1c1c"/><rect x="3" y="4" width="6" height="4.2" fill="none" stroke="#fff" stroke-width=".9"/><path d="M3 4l3 2.3L9 4" fill="none" stroke="#fff" stroke-width=".9"/></svg>
          marco@velvetharborphotography.com
        </span>
      </p>
      <p class="contact-line">
        <span class="contact-item">
          <svg viewBox="0 0 12 12" aria-hidden="true"><circle cx="6" cy="6" r="6" fill="#1c1c1c"/><circle cx="6" cy="6" r="3.4" fill="none" stroke="#fff" stroke-width=".8"/><path d="M2.6 6h6.8M6 2.6c-1.6 2-1.6 4.8 0 6.8M6 2.6c1.6 2 1.6 4.8 0 6.8" fill="none" stroke="#fff" stroke-width=".7"/></svg>
          www.velvetharborphotography.com
        </span>
      </p>
    </div>
  </section>

</main>
</body>
</html>
```